Business Cards for new orthopaedic surgery practice

My husband and I are starting our own orthopaedic surgery practice. We are looking for a business card that is uniform, but one will have my name/title and the other will have his. You can just create one design with my name on it for now. But when I choose your design as the winning design I will ask that you add another copy with his name/title.

We are looking for classy, simple, elite all in one. We like dark blues/a little gold/yellow. Something that goes with our logo. We want our logo incorporated. Here is all the info you need:
Business name: RV Spine & Vitality Center
Location: 38915 North Bramble Ave
Larkfield, FL 34812
Phone: 954-218-4630
Fax: 954-571-2846
Email: info@myrvspine.example

Names: Lucinda Ferrow, M.D.
Board Certified Hand and Upper Extremity Surgeon

Emeka Dlunga, M.D.
Board Certified Hip & Knee Replacement/General Orthopaedic Surgeon

Can decide what you want to put on the back. Maybe a slogan:
Rooted in Care. Focused on You

I am just going to upload our logo. The only thing is if we select you as the winning design, the location, and phone numbers may change. We will need your help to update that once fully solidified.

Industry/Entity Type

Medical

Contact Information for Business Card

Colors
0054AA
0677BA
7BADD7
CADEEF
E8F1F8
0094D4
00A9DD
6FCCEA
C7EBF8
E9F6FB

Requirements
Must have
• class, appeal,
Should not have
• We want to air on the side of masculine if we are looking at masculine vs. feminine feel. But we still want it classy, sophisticated, and something we will love

```html
<!DOCTYPE html>
<html lang="en">
<head>
<meta charset="utf-8">
<title>RV Spine &amp; Vitality Center — Business Card</title>
<link href="https://fonts.googleapis.com/css2?family=Source+Serif+4:opsz,wght@8..60,400;8..60,600;8..60,700&display=swap" rel="stylesheet">
<style>
  :root {
    --navy: #1b2a4e;
    --gold: #c8a45e;
    --paper: #ffffff;
    --backdrop: #e9e9e7;
  }
  html, body {
    margin: 0;
    padding: 0;
    width: 1200px;
    height: 579px;
    overflow: hidden;
    background: var(--backdrop);
    font-family: "Source Serif 4", Georgia, serif;
  }
  .sheet {
    position: relative;
    width: 1200px;
    height: 579px;
  }
  .card {
    position: absolute;
    top: 129px;
    width: 540px;
    height: 321px;
    box-shadow: 0 2px 8px rgba(0,0,0,0.12);
    overflow: hidden;
  }
  .card--front { left: 40px; background: var(--paper); }
  .card--back { left: 620px; background: var(--gold); }

  .holder { position: absolute; left: 56px; top: 64px; color: var(--navy); }
  .holder__name { margin: 0; font-size: 20px; font-weight: 700; line-height: 1.1; }
  .holder__title { margin: 3px 0 0; font-size: 10.5px; font-weight: 600; }
  .divider {
    position: absolute; left: 56px; top: 130px;
    width: 211px; height: 2px; background: var(--gold);
  }
  .contact {
    position: absolute; left: 56px; top: 174px;
    margin: 0; padding: 0; list-style: none;
    color: var(--navy); font-size: 11.5px; font-weight: 600; line-height: 1.2;
  }
  .contact__item { display: flex; align-items: flex-start; margin-bottom: 9px; }
  .contact__icon { width: 10px; height: 10px; margin: 2px 13px 0 0; flex: none; }

  .band { position: absolute; left: 381px; width: 100px; }
  .band--navy { top: 0; height: 161px; background: var(--navy); }
  .band--gold { top: 161px; height: 160px; background: var(--gold); }
  .seal {
    position: absolute; left: 370px; top: 100px;
    width: 122px; height: 122px; border-radius: 50%;
    background: var(--paper);
    display: flex; align-items: center; justify-content: center;
  }
  .brand {
    margin: 0; text-align: center; color: var(--navy);
    font-weight: 700; font-size: 13px; line-height: 1.2;
  }
  .brand--back { font-size: 22px; }

  .ring {
    position: absolute; left: 50%; top: 50%;
    width: 180px; height: 180px; margin: -90px 0 0 -90px;
    border: 2px solid var(--navy); border-radius: 50%;
    display: flex; align-items: center; justify-content: center;
    box-sizing: border-box;
  }
</style>
</head>
<body>
<main class="sheet">
  <section class="card card--front" aria-label="Card front">
    <div class="holder">
      <h1 class="holder__name">Lucinda Ferrow, M.D.</h1>
      <p class="holder__title">Board Certified Hand and Upper Extremity Surgeon</p>
    </div>
    <div class="divider"></div>
    <ul class="contact">
      <li class="contact__item">
        <svg class="contact__icon" viewBox="0 0 10 10"><path d="M5 0.5a3.3 3.3 0 0 0-3.3 3.3C1.7 6.3 5 9.5 5 9.5s3.3-3.2 3.3-5.7A3.3 3.3 0 0 0 5 0.5z" fill="#c8a45e"/><circle cx="5" cy="3.8" r="1.2" fill="#fff"/></svg>
        <span>38915 North Bramble Ave<br>Larkfield, FL 34812</span>
      </li>
      <li class="contact__item">
        <svg class="contact__icon" viewBox="0 0 10 10"><path d="M2.2 0.8l1.6 2-1 1.1a6 6 0 0 0 3.3 3.3l1.1-1 2 1.6-1 1.6C4.8 9.3 0.7 5.2 0.6 1.8z" fill="none" stroke="#c8a45e" stroke-width="0.9"/></svg>
        <span>954-218-4630</span>
      </li>
      <li class="contact__item">
        <svg class="contact__icon" viewBox="0 0 10 10"><rect x="2.5" y="0.8" width="5" height="3" fill="none" stroke="#c8a45e" stroke-width="0.9"/><rect x="0.8" y="3.8" width="8.4" height="3.6" rx="0.6" fill="#c8a45e"/><rect x="2.5" y="6.3" width="5" height="2.9" fill="#fff" stroke="#c8a45e" stroke-width="0.9"/></svg>
        <span>954-571-2846</span>
      </li>
      <li class="contact__item">
        <svg class="contact__icon" viewBox="0 0 10 10"><rect x="0.8" y="2" width="8.4" height="6" fill="none" stroke="#c8a45e" stroke-width="0.9"/><path d="M0.8 2L5 5.4 9.2 2" fill="none" stroke="#c8a45e" stroke-width="0.9"/></svg>
        <span>info@myrvspine.example</span>
      </li>
    </ul>
    <div class="band band--navy"></div>
    <div class="band band--gold"></div>
    <div class="seal">
      <p class="brand">RV Spine &amp;<br>Vitality<br>Center</p>
    </div>
  </section>

  <section class="card card--back" aria-label="Card back">
    <div class="ring">
      <p class="brand brand--back">RV Spine &amp;<br>Vitality<br>Center</p>
    </div>
  </section>
</main>
</body>
</html>
```